Bluestone Advisory & Mgmt - Professional Business Cards

Hi!

I am a Real Estate Developer and Construction Consultant.

I have a lot of inspiration from previous designs and would be open to using the attached Designs as a starting point. I would like to see these styles incorporated into your designs.

I really need professional business card to go with it that includes my important info.

Look forward to seeing your designs!.

Target Market(s)

My Target market are building owners, lawyers, consultants.

Industry/Entity Type

Real Estate Development

Contact Information for Business Card

My Name: Dorian Pelkey
My Title: Principle
Company Name: Bluestone Advisory & Mgmt, LLC
Address: 348 West 71st Street, 9th FL New York, NY 10010
Mobile: 917.806.3971
Website: bam-hvx.example

Font styles to use
Serif
Sans Serif

Colors

Designer to choose colors to be used in the design.

Requirements
Must have
• Must incorporate the logo attached or have new that looks similar.
• Must use professional font that will be seen and judged by wealthy land owners and developers.
• Must incorporate some of the color green.
Should not have
• Photo's or pictures of people or buildings of any kind.

```html
<!DOCTYPE html>
<html lang="en">
<head>
<meta charset="UTF-8">
<title>Bluestone Advisory &amp; Mgmt - Professional Business Cards</title>
<link href="https://fonts.googleapis.com/css2?family=Open+Sans:ital,wght@0,400;0,600;0,700;1,700&display=swap" rel="stylesheet">
<style>
  :root {
    --green-deep: #249a57;
    --green-mid: #3dbb72;
    --green-light: #5fd68f;
    --grey-text: #8f8888;
    --ink: #3a3a3a;
    --paper: #ffffff;
    --backdrop: #e9ecea;
  }
  * { box-sizing: border-box; margin: 0; padding: 0; }
  html, body {
    width: 1200px; height: 900px; overflow: hidden;
    background: var(--backdrop);
    font-family: "Open Sans", Arial, sans-serif;
  }
  .sheet {
    position: relative; width: 1200px; height: 900px;
    display: flex; align-items: center; justify-content: center; gap: 40px;
  }
  .card {
    position: relative; width: 540px; height: 309px;
    border-radius: 22px; overflow: hidden;
    box-shadow: 0 10px 26px rgba(0,0,0,.14);
    background: var(--paper);
  }
  /* contact side */
  .card--contact { border: 9px solid var(--green-mid); }
  .contact-list {
    position: absolute; left: 26px; top: 100px; width: 280px;
    color: var(--ink); font-size: 12.5px; line-height: 1.55;
  }
  .contact-company {
    color: var(--green-deep); font-weight: 700; font-size: 14px;
    padding-bottom: 6px; margin-bottom: 8px;
    border-bottom: 1px solid transparent;
    border-image: linear-gradient(90deg, var(--green-mid), rgba(61,187,114,0)) 1;
  }
  .contact-row { display: flex; align-items: flex-start; gap: 8px; margin-bottom: 3px; }
  .contact-row svg { flex: none; margin-top: 3px; }
  .contact-inline { display: flex; gap: 16px; }
  .contact-inline span { display: flex; align-items: center; gap: 8px; }
  .brand-name {
    color: var(--grey-text); font-weight: 600; line-height: 1.15;
    display: flex; align-items: center; gap: 10px;
  }
  .brand-mark { width: 14px; height: 14px; background: var(--green-mid); flex: none; }
  .card--contact .brand-name {
    position: absolute; right: 22px; top: 140px; font-size: 20px; width: 168px;
  }
  /* name side */
  .card--name { background: linear-gradient(160deg, var(--green-deep), var(--green-light)); }
  .card--name svg.card-shape { position: absolute; inset: 0; }
  .card--name .brand-name {
    position: absolute; left: 36px; top: 66px; font-size: 22px; width: 210px;
  }
  .card-web {
    position: absolute; left: 60px; top: 160px; font-size: 12.5px; font-weight: 700;
    color: var(--ink); padding-top: 8px; width: 170px;
    border-top: 1px solid var(--green-mid);
  }
  .holder {
    position: absolute; right: 26px; top: 96px; color: var(--paper); text-align: left;
  }
  .holder-name { font-weight: 700; font-style: italic; font-size: 20px; white-space: nowrap; }
  .holder-title {
    font-size: 14px; margin-top: 4px; padding-top: 4px;
    border-top: 1px solid rgba(255,255,255,.55);
  }
</style>
</head>
<body>
<main class="sheet">
  <article class="card card--contact">
    <div class="contact-list">
      <div class="contact-company">Bluestone Advisory &amp; Mgmt, LLC</div>
      <div class="contact-row">
        <svg width="12" height="14" viewBox="0 0 12 14" aria-hidden="true"><path d="M6 0a5 5 0 0 0-5 5c0 4 5 9 5 9s5-5 5-9a5 5 0 0 0-5-5zm0 7a2 2 0 1 1 0-4 2 2 0 0 1 0 4z" fill="#3dbb72"/></svg>
        <span>348 West 71st Street, 9th FL New York, NY 10010</span>
      </div>
      <div class="contact-row contact-inline">
        <span><svg width="12" height="12" viewBox="0 0 12 12" aria-hidden="true"><path d="M2.5 0l2 3-1.2 1.4a7 7 0 0 0 4.3 4.3L9 7.5l3 2-1 2.5C5 12 0 7 0 1z" fill="#3dbb72"/></svg>917.806.3971</span>
        <span><svg width="12" height="12" viewBox="0 0 12 12" aria-hidden="true"><circle cx="6" cy="6" r="5" fill="none" stroke="#3dbb72" stroke-width="1.6"/><path d="M1 6h10M6 1c2.5 3 2.5 7 0 10M6 1c-2.5 3-2.5 7 0 10" fill="none" stroke="#3dbb72" stroke-width="1"/></svg>www.bam-hvx.example</span>
      </div>
    </div>
    <div class="brand-name"><span class="brand-mark"></span><span>Bluestone Advisory Management</span></div>
  </article>

  <article class="card card--name">
    <svg class="card-shape" width="540" height="309" viewBox="0 0 540 309" aria-hidden="true">
      <path d="M270 0 C 370 60 370 240 220 309 L 560 309 L 560 0 Z" fill="rgba(255,255,255,.08)"/>
      <path d="M300 210 C 400 185 490 205 540 245 L 540 309 L 260 309 Z" fill="rgba(255,255,255,.1)"/>
      <path d="M0 0 H245 C 345 45 350 235 215 309 H0 Z" fill="#ffffff"/>
    </svg>
    <div class="brand-name"><span class="brand-mark"></span><span>Bluestone Advisory Management</span></div>
    <div class="card-web">www.bam-hvx.example</div>
    <div class="holder">
      <div class="holder-name">Dorian Pelkey</div>
      <div class="holder-title">Principle</div>
    </div>
  </article>
</main>
</body>
</html>
```